Web Design for an Online Dating Web Site

We need an uncoded web design for a new online dating web site called zMatchy.net. Simplicity and boldness are the key factors in the successful design.
Please look at the requirements document attached for details.
Updates
Dear all,
Please AVOID USING A PICTURE OF A HAPPY COUPLE ON THE HOME PAGE of the site. We highly want to move away from this space as it makes our web site just like another dating web site.
We like something simple with web 2.0 look and feel. The examples in the Requirements Document are exactly the design we are after.
Regards
Tarn
Industry/Entity Type
Dating
Look and feel
Each slider illustrates characteristics of the customer's brand and the style your logo design should communicate.

```html
<!DOCTYPE html>
<html lang="en">
<head>
<meta charset="utf-8">
<title>zMatchy.net – Home</title>
<link href="https://fonts.googleapis.com/css2?family=Ubuntu:ital,wght@0,300;0,400;0,500;0,700;1,400;1,500&family=Arimo:wght@400;700&display=swap" rel="stylesheet">
<style>
:root{
  --lime:#c3e35a;
  --lime-light:#e6f5b4;
  --lime-dark:#9cc038;
  --olive:#8fb42a;
  --ink:#3b3b2c;
  --pink:#e73d8e;
  --pink-dark:#cf2a78;
  --teal:#3fb0bf;
  --teal-dark:#2a9aa9;
  --text:#555;
  --rule:#dcdcdc;
  --side:#f4f4f4;
  --foot:#2a2a2a;
  --foot-field:#383838;
  --foot-text:#e8e8e8;
  --fb-blue:#3b5998;
}
*{margin:0;padding:0;box-sizing:border-box}
html,body{width:1200px;height:1039px;overflow:hidden}
body{position:relative;font-family:"Arimo",Arial,sans-serif;background:#fff;color:var(--text)}
.abs{position:absolute}

/* header */
.site-header{position:absolute;left:0;top:0;width:1200px;height:145px;background:var(--lime);border-bottom:1px solid var(--lime-dark)}
.brand{position:absolute;left:137px;top:14px;display:flex;align-items:center;gap:8px;font-family:"Ubuntu",sans-serif;font-weight:700;font-size:44px;color:var(--pink);letter-spacing:-1px}
.brand-dot{width:22px;height:22px;border-radius:50%;background:var(--pink)}
.main-nav a{position:absolute;top:16px;width:110px;margin-left:-55px;text-align:center;font-family:"Ubuntu",sans-serif;font-weight:300;font-size:14.5px;color:#93b93a;text-decoration:none}
.main-nav svg{display:block;margin:0 auto 4px}
.signup-blob{position:absolute;left:900px;top:-10px;width:152px;height:68px;border-radius:0 0 76px 76px/0 0 50px 50px;background:var(--pink);color:#fff;font-family:"Ubuntu",sans-serif;font-weight:500;font-size:22px;text-align:center;padding-top:18px;letter-spacing:.5px}
.field{position:absolute;height:34px;background:#fff;border-radius:6px;border:2px solid #eaf6c4;font-family:"Ubuntu",sans-serif;font-weight:300;font-size:13px;color:#aaa;padding:9px 14px}
.btn-login{position:absolute;left:545px;top:93px;width:80px;height:32px;background:var(--pink);border-radius:3px;color:#fff;font-family:"Ubuntu",sans-serif;font-size:18px;text-align:center;line-height:32px}
.or{position:absolute;left:650px;top:88px;font-family:"Ubuntu",sans-serif;font-size:34px;color:#fff}
.social{position:absolute;top:96px;width:26px;height:26px;border-radius:50%}
.btn-view{position:absolute;left:960px;top:93px;width:80px;height:32px;background:#e2f3a3;border-radius:3px;color:#9fc64a;font-family:"Ubuntu",sans-serif;font-size:14px;text-align:center;line-height:32px}

/* hero */
.hero{position:absolute;left:0;top:146px;width:1200px;height:306px;background:linear-gradient(180deg,var(--lime-light) 0%,#e4f3a9 45%,var(--lime) 100%);overflow:hidden}
.hero-title{position:absolute;left:137px;top:20px;font-family:"Ubuntu",sans-serif;font-size:44px;color:var(--olive)}
.perks{list-style:none;position:absolute;left:150px;top:86px}
.perks li{display:flex;align-items:center;height:48px;font-family:"Ubuntu",sans-serif;font-size:22px;color:var(--olive)}
.perks b{color:var(--ink);font-weight:500}
.perk-num{width:27px;height:27px;border-radius:50%;border:2px solid var(--olive);color:var(--olive);font-size:14px;font-style:italic;text-align:center;line-height:23px;margin-right:17px}
.reel{position:absolute;left:539px;top:78px;width:97px;height:166px;border-radius:48px 0 0 48px;background:radial-gradient(circle at 40% 45%,#f4f4f0,#bdbdb4 60%,#8f8f86)}
.video{position:absolute;left:630px;top:25px;width:391px;height:219px;background:linear-gradient(120deg,#3a3f3c,#1c1f1d 60%,#2b2f2c)}
.video-bar{position:absolute;left:6px;bottom:6px;right:6px;height:24px;background:rgba(0,0,0,.75);display:flex;align-items:center;padding:0 8px;gap:8px}
.video-bar .track{flex:1;height:6px;border:1px solid #888}
.video-bar .hd{color:#4aa3e8;font:italic 700 10px "Arimo",sans-serif}
.video-time{position:absolute;left:45px;bottom:27px;background:#fff;color:#111;font-size:7px;padding:0 2px}
.video-shadow{position:absolute;left:680px;top:246px;width:300px;height:30px;border-radius:50%;background:rgba(120,150,40,.35);filter:blur(8px)}
.slide-arrow{position:absolute;top:26px;width:90px;height:90px;border-radius:50%;background:#c5e8ee;color:#3f9fb3;font-size:24px;line-height:90px;font-family:"Ubuntu",sans-serif}
.dots{position:absolute;left:478px;top:271px;display:flex;gap:11px}
.dots span{width:13px;height:13px;border-radius:50%;border:1px solid #5fa5b0}
.dots span.on{background:#5b9cc0}
.zig{position:absolute;left:0;width:1200px;height:8px}

/* content */
.sidebar-bg{position:absolute;left:793px;top:452px;width:407px;height:366px;background:linear-gradient(90deg,#ececec,#fafafa 40px,#fff)}
.card{position:absolute;top:481px;width:263px}
.card-img{width:263px;height:93px}
.card h2{font-family:"Ubuntu",sans-serif;font-weight:400;font-size:18px;color:var(--teal);margin-top:10px;padding-bottom:4px;border-bottom:1px solid var(--rule)}
.card p{font-size:9.3px;line-height:14.5px;color:#666;margin:11px 2px 0}
.btn-read{display:block;margin:12px auto 0;width:99px;height:28px;border-radius:6px;background:linear-gradient(#58c4d0,var(--teal-dark));color:#e6fbff;font-family:"Ubuntu",sans-serif;font-size:14px;text-align:center;line-height:28px}
.blog{position:absolute;left:830px;top:475px;width:205px}
.blog h3{font-family:"Ubuntu",sans-serif;font-weight:400;font-size:19px;color:#333}
.post{position:absolute;left:0;width:205px;height:64px}
.post-thumb{position:absolute;left:1px;top:0;width:60px;height:60px;border-radius:50%;border:2px solid #fff;box-shadow:0 1px 3px rgba(0,0,0,.35)}
.post a{position:absolute;left:74px;top:8px;width:110px;font-family:"Ubuntu",sans-serif;font-size:13px;line-height:15px;color:var(--pink);text-decoration:none;border-bottom:1px dashed #ccc;padding-bottom:2px}
.post time{position:absolute;right:22px;font:italic 8.5px "Arimo",sans-serif;color:#444}
.blog-more{position:absolute;right:0;top:288px;font:italic 700 10px "Arimo",sans-serif;color:#333}

/* footer */
.site-footer{position:absolute;left:0;top:817px;width:1200px;height:222px;background:var(--foot);color:var(--foot-text)}
.site-footer h4{position:absolute;top:25px;font-family:"Ubuntu",sans-serif;font-weight:500;font-size:13px;color:#fff}
.foot-links{position:absolute;left:154px;top:45px;list-style:none;font-size:10px}
.foot-links li{height:22px;line-height:22px}
.foot-links li::before{content:"›";color:var(--teal);margin-right:6px}
.copy{position:absolute;left:154px;top:178px;font-size:8.5px}
.dark-field{position:absolute;background:var(--foot-field);border-radius:5px;font-size:9.5px;color:#999;padding:10px 12px;overflow:hidden}
.ghost-brand{position:absolute;left:70px;top:22px;font-family:"Ubuntu",sans-serif;font-weight:700;font-size:34px;color:#4a3039}
.btn-send{position:absolute;left:481px;top:175px;width:99px;height:29px;border-radius:6px;background:linear-gradient(#4a4a4a,#2f2f2f);border:1px solid #1e1e1e;color:#eee;font-family:"Ubuntu",sans-serif;font-size:12px;text-align:center;line-height:27px}
.fan-box{position:absolute;left:820px;top:23px;width:201px;height:170px;background:#fff;border:1px solid #aab8d4;color:#333;font-family:"Arimo",sans-serif}
.fan-box header{height:26px;background:#edeff4;border-bottom:1px solid #c4cde0;font-size:10px;font-weight:700;padding:7px 9px;color:#333}
.fan-page{position:absolute;left:9px;top:34px;width:30px;height:32px;background:linear-gradient(#9a7a5a,#4d3a2a)}
.fan-name{position:absolute;left:49px;top:35px;width:145px;font-size:11.5px;font-weight:700;color:var(--fb-blue);line-height:12px}
.fan-like{position:absolute;left:49px;top:76px;font-size:8.5px}
.fan-like span{color:var(--fb-blue)}
.fan-count{position:absolute;left:9px;top:99px;right:6px;border-top:1px solid #ddd;padding-top:7px;font-size:8.5px;line-height:10px}
.fans{position:absolute;left:9px;top:128px;display:flex;gap:4px}
.fans figure{width:41px;text-align:center;font-size:7px;color:#666}
.fans .ph{width:41px;height:40px;margin-bottom:3px}
</style>
</head>
<body>

<header class="site-header">
  <div class="brand"><span>zMatchy</span><span class="brand-dot"></span></div>

  <nav class="main-nav">
    <a style="left:477px"><svg width="18" height="20" viewBox="0 0 18 20"><text x="9" y="17" text-anchor="middle" font-family="Ubuntu" font-weight="700" font-size="20" fill="#9cc038">?</text></svg>Why</a>
    <a style="left:588px"><svg width="24" height="20" viewBox="0 0 24 20"><text x="12" y="17" text-anchor="middle" font-family="Ubuntu" font-weight="700" font-size="20" fill="#9cc038">!?</text></svg>How It Works</a>
    <a style="left:696px"><svg width="18" height="20" viewBox="0 0 18 20"><path d="M9 2 L16 10 H12 V17 H6 V10 H2 Z" fill="#9cc038"/></svg>Sign Up</a>
    <a style="left:809px"><svg width="22" height="20" viewBox="0 0 22 20"><rect x="2" y="4" width="14" height="14" fill="none" stroke="#9cc038" stroke-width="2"/><path d="M9 12 L18 2 L21 4 L12 14 Z" fill="#9cc038"/></svg>Our Blog</a>
  </nav>

  <div class="signup-blob">SIGN UP</div>

  <div class="field" style="left:137px;top:92px;width:183px">Username</div>
  <div class="field" style="left:340px;top:92px;width:183px">Password</div>
  <div class="btn-login">Log in</div>
  <div class="or">Or</div>
  <span class="social" style="left:713px;background:#3d69b3"></span>
  <span class="social" style="left:757px;background:#55c1e8"></span>
  <span class="social" style="left:802px;background:#7b2b8e"></span>
  <span class="social" style="left:846px;background:#f4f4f4"></span>
  <svg class="abs" style="left:888px;top:96px" width="48" height="20" viewBox="0 0 48 20"><path d="M2 14 Q22 4 42 9" fill="none" stroke="#9cc038" stroke-width="3" stroke-linecap="round"/><path d="M34 3 L43 9 L35 15" fill="none" stroke="#9cc038" stroke-width="3" stroke-linecap="round"/></svg>
  <div class="btn-view">View more</div>
</header>

<section class="hero">
  <div class="slide-arrow" style="left:-30px;text-align:right;padding-right:35px">‹</div>
  <div class="slide-arrow" style="left:1140px;padding-left:32px">›</div>

  <h1 class="hero-title">Why we are better?</h1>
  <ul class="perks">
    <li><span class="perk-num">1</span><b>Lorem Ipsum</b>&nbsp;is simply dummy text</li>
    <li><span class="perk-num">2</span>It is a long&nbsp;<b>established fact</b></li>
    <li><span class="perk-num">3</span><b>There</b>&nbsp;are many variations</li>
  </ul>

  <div class="video-shadow"></div>
  <div class="reel" role="img" aria-label="Illustration of a film reel with a popcorn box"></div>
  <div class="video" role="img" aria-label="Video still of a man speaking to camera">
    <span class="video-time">00:59</span>
    <div class="video-bar">
      <svg width="10" height="12" viewBox="0 0 10 12"><path d="M1 1 L9 6 L1 11 Z" fill="#fff"/></svg>
      <span class="track"></span>
      <span class="hd">HD</span>
    </div>
  </div>

  <div class="dots"><span class="on"></span><span></span><span></span></div>

  <svg class="zig" style="top:298px" viewBox="0 0 1200 8" preserveAspectRatio="none">
    <defs><pattern id="teethDown" width="8" height="8" patternUnits="userSpaceOnUse"><path d="M0 8 L4 2 L8 8 Z" fill="#fff"/></pattern></defs>
    <rect width="1200" height="8" fill="url(#teethDown)"/>
  </svg>
</section>

<div class="sidebar-bg"></div>

<article class="card" style="left:144px">
  <div class="card-img" role="img" aria-label="Photo of a bubble bath with champagne and flowers" style="background:linear-gradient(180deg,#8a6a4e,#c9b8a5 55%,#e8e2dc)"></div>
  <h2>Contrary to popular belief</h2>
  <p>But I must explain to you how all this mistaken idea of denouncing pleasure and praising pain was born and I will give you a complete account of the system, and expound the actual teachings of the great explorer of the truth, the master-builder of human happiness. No one rejects, dislikes, or avoids pleasure itself</p>
  <span class="btn-read">Read more</span>
</article>

<article class="card" style="left:455px">
  <div class="card-img" role="img" aria-label="Close-up photo of skin and an eye" style="background:linear-gradient(90deg,#f2a58a,#e9937a 70%,#b8705e)"></div>
  <h2>There are many variations</h2>
  <p>On the other hand, we denounce with righteous indigna-tion and dislike men who are so beguiled and demoralized by the charms of pleasure of the moment, so blinded by desire, that they cannot foresee the pain and trouble that are bound to ensue; and equal blame belongs to those who fail in their duty through</p>
  <span class="btn-read">Read more</span>
</article>

<aside class="blog">
  <h3>Latest Blog Post</h3>
  <div class="post" style="top:35px">
    <div class="post-thumb" role="img" aria-label="Photo of a skyscraper against the sky" style="background:radial-gradient(circle,#7e8a99,#dfe6ee)"></div>
    <a>On the other hand</a><time style="top:37px">Jul 27, 2011</time>
  </div>
  <div class="post" style="top:116px">
    <div class="post-thumb" role="img" aria-label="Photo of an ancient stone relief" style="background:radial-gradient(circle,#a8916a,#d8c9a8)"></div>
    <a>With righteous indignation like</a><time style="top:52px">Jul 27, 2011</time>
  </div>
  <div class="post" style="top:197px">
    <div class="post-thumb" role="img" aria-label="Photo of a wristwatch" style="background:radial-gradient(circle,#eeeeee,#7a6a5e)"></div>
    <a>Choice is untrammelled</a><time style="top:52px">Jul 27, 2011</time>
  </div>
  <div class="blog-more">› View more Blog Posts</div>
</aside>

<footer class="site-footer">
  <svg class="zig" style="top:-8px" viewBox="0 0 1200 8" preserveAspectRatio="none">
    <defs><pattern id="teethUp" width="8" height="8" patternUnits="userSpaceOnUse"><path d="M0 8 L4 2 L8 8 Z" fill="#2a2a2a"/></pattern></defs>
    <rect width="1200" height="8" fill="url(#teethUp)"/>
  </svg>

  <h4 style="left:154px">Read more</h4>
  <ul class="foot-links">
    <li>Why zMatchy</li>
    <li>How it works</li>
    <li>Sign Up</li>
    <li>Login</li>
    <li>About Us</li>
  </ul>
  <p class="copy">© 2011 by zMatchy.net All Rights Reserved.</p>

  <h4 style="left:377px">Let's Talk</h4>
  <div class="dark-field" style="left:375px;top:52px;width:153px;height:26px;padding-top:8px">Name</div>
  <div class="dark-field" style="left:543px;top:52px;width:153px;height:26px;padding-top:8px">E-mail Address</div>
  <div class="dark-field" style="left:375px;top:86px;width:322px;height:81px">Comment<span class="ghost-brand">zMatchy</span></div>
  <div class="btn-send">Send Message</div>

  <div class="fan-box">
    <header>Find us on Friendbook</header>
    <div class="fan-page" role="img" aria-label="Fan page profile photo"></div>
    <div class="fan-name">The Riverbend Fan Club</div>
    <div class="fan-like">You like this. &nbsp;<span>Unlike</span></div>
    <div class="fan-count">836 people like The Riverbend Fan Club</div>
    <div class="fans">
      <figure><div class="ph" role="img" aria-label="Member photo" style="background:linear-gradient(#b7b9b0,#6f7468)"></div>Oskar</figure>
      <figure><div class="ph" role="img" aria-label="Member photo" style="background:linear-gradient(#c9966a,#7d5336)"></div>Bennet</figure>
      <figure><div class="ph" role="img" aria-label="Member photo" style="background:linear-gradient(#d8b09a,#8a5e4a)"></div>Rafe</figure>
      <figure><div class="ph" role="img" aria-label="Member photo" style="background:linear-gradient(#cdbfb2,#8a7466)"></div>Ivo</figure>
    </div>
  </div>
</footer>

</body>
</html>
```